new business card and logo for a high end Automotive repair and performance shop

Need to update our design for our business cards. New address, and want a new look. I'll upload some pics of our current card. We are a high end auto repair/tuning shop. New address will be 5812 W. Birch Ln Killeen, T.X. 76542. I do have the vector files if needed. The logo would have a similar design. Love the look of carbon fiber, and brushed aluminum, although may have issues showing the texture of the material due to dpi restrictions during card printing. Also the logo would have to be easily printed on shirts, and for embroidery. Thanks, and good luck.

www.motor-zenith.com

Target Market(s)

High end automotive repair, dealership alternative.

Industry/Entity Type

Automotive

Contact Information for Business Card

MOTORZENITH
5812 W. BIRCH LN
KILLEEN, T.X. 76542
PH 612-555-0193
FAX 612-555-0147
EMAIL INFO@MOTOR-ZENITH.COM

Logo Text

MotorZenith

Font styles to use
Sans Serif

Requirements
Must have
• name, address, description that was uploaded.
Nice to have
• maybe some brands i.e. veltra, norvex, Calvaro, krd, solmara, vorin etc. not necessary. simple is good, like the look of carbon fiber, brushed aluminum.
Should not have
• open to all suggestions.

```html
<!DOCTYPE html>
<html lang="en">
<head>
<meta charset="utf-8">
<title>MotorZenith Business Card</title>
<link rel="stylesheet" href="https://fonts.googleapis.com/css2?family=Arimo:wght@400;700&family=Open+Sans:wght@400;600&family=Tinos:wght@700&display=swap">
<style>
  :root {
    --page-bg: #262626;
    --carbon-dark: #121212;
    --carbon-mid: #232323;
    --panel-light: #f4f4f4;
    --panel-light-edge: #dcdcdc;
    --accent-red: #d71f26;
    --ink-dark: #222222;
    --ink-light: #e6e6e6;
    --ink-grey: #cfcfcf;
  }
  * { box-sizing: border-box; margin: 0; padding: 0; }
  html, body { width: 1200px; height: 997px; overflow: hidden; }
  body {
    background: var(--page-bg);
    font-family: "Arimo", Arial, sans-serif;
  }
  .canvas {
    position: relative;
    width: 1200px;
    height: 997px;
  }
  .card {
    position: absolute;
    left: 220px;
    width: 760px;
    height: 434px;
    border-radius: 24px;
    overflow: hidden;
    display: grid;
    grid-template-columns: 1fr 1fr;
    grid-template-rows: 1fr 1fr;
    box-shadow: 0 10px 30px rgba(0,0,0,0.55);
  }
  .card--back { top: 52px; }
  .card--front { top: 511px; }

  .panel { position: relative; display: flex; flex-direction: column; justify-content: center; }
  .panel--carbon { background: linear-gradient(160deg, var(--carbon-mid), var(--carbon-dark)); }
  .panel--light { background: linear-gradient(160deg, #ffffff, var(--panel-light) 60%, var(--panel-light-edge)); }

  .brand {
    display: flex; align-items: center; justify-content: center; gap: 12px; height: 100%;
  }
  .brand__mark {
    width: 26px; height: 26px; background: var(--accent-red);
  }
  .brand__name {
    font-family: "Arimo", Arial, sans-serif;
    font-weight: 700;
    font-size: 26px;
    letter-spacing: 2px;
    color: var(--ink-dark);
  }

  .specialties {
    padding: 0 40px;
    font-family: "Open Sans", Arial, sans-serif;
    font-size: 15px;
    line-height: 1.75;
    letter-spacing: 1px;
    color: var(--ink-grey);
    text-transform: uppercase;
  }
  .hours {
    align-items: center;
    text-align: center;
    font-family: "Open Sans", Arial, sans-serif;
    font-size: 16px;
    line-height: 1.8;
    color: var(--accent-red);
    text-transform: uppercase;
  }
  .website {
    justify-content: flex-end;
    padding: 0 0 34px 30px;
    font-family: "Arimo", Arial, sans-serif;
    font-weight: 700;
    font-size: 17px;
    letter-spacing: 1.5px;
    color: var(--accent-red);
  }

  .person { padding-left: 70px; }
  .person__name {
    font-family: "Tinos", "Times New Roman", serif;
    font-weight: 700;
    font-size: 34px;
    color: var(--accent-red);
  }
  .person__title {
    margin-top: 2px; padding-left: 56px;
    font-size: 20px; color: var(--ink-light);
  }

  .contacts { list-style: none; padding-left: 46px; }
  .contacts li {
    display: flex; align-items: center; gap: 20px;
    font-size: 18px; color: var(--ink-dark); line-height: 2;
  }
  .contacts svg { width: 16px; height: 16px; fill: var(--accent-red); flex: none; }

  .company { align-items: center; text-align: center; }
  .company__name { font-size: 22px; color: var(--ink-light); }
  .company__address { margin-top: 10px; font-size: 15px; color: var(--accent-red); }
</style>
</head>
<body>
<main class="canvas">

  <section class="card card--back" aria-label="Card back">
    <div class="panel panel--light">
      <div class="brand">
        <span class="brand__mark"></span>
        <span class="brand__name">MOTORZENITH</span>
      </div>
    </div>
    <div class="panel panel--carbon">
      <p class="specialties">Specializing in<br>Asian, European &amp;<br>Domestic vechicle repair,<br>service,<br>fabrication &amp; performance.</p>
    </div>
    <div class="panel panel--carbon website">http://www.motor-zenith.com/</div>
    <div class="panel panel--light hours">
      <p>Monday - Friday<br>7:00 AM - 6:00 PM<br>Sunday Closed<br>Book your appointment now</p>
    </div>
  </section>

  <section class="card card--front" aria-label="Card front">
    <div class="panel panel--carbon person">
      <p class="person__name">Dale Rourke</p>
      <p class="person__title">Owner</p>
    </div>
    <div class="panel panel--light">
      <div class="brand">
        <span class="brand__mark"></span>
        <span class="brand__name">MOTORZENITH</span>
      </div>
    </div>
    <div class="panel panel--light">
      <ul class="contacts">
        <li>
          <svg viewBox="0 0 16 16" aria-hidden="true"><path d="M4 0h8a1 1 0 0 1 1 1v14a1 1 0 0 1-1 1H4a1 1 0 0 1-1-1V1a1 1 0 0 1 1-1zm1 2v10h6V2zm3 11a1 1 0 1 0 0 2 1 1 0 0 0 0-2z"/></svg>
          612-555-0193
        </li>
        <li>
          <svg viewBox="0 0 16 16" aria-hidden="true"><path d="M4 1h8v4H4zM1 6h14v7h-3v2H4v-2H1zm4 5v3h6v-3z"/></svg>
          612-555-0147
        </li>
        <li>
          <svg viewBox="0 0 16 16" aria-hidden="true"><path d="M1 3h14v10H1zm1.5 1.2L8 8.6l5.5-4.4z"/></svg>
          info@motor-zenith.com
        </li>
      </ul>
    </div>
    <div class="panel panel--carbon company">
      <p class="company__name">Motor-Zenith</p>
      <p class="company__address">5812 W. Birch Ln Brookvale, TX. 75019</p>
    </div>
  </section>

</main>
</body>
</html>
```